Wilderness Doc & TV personality personal page

I’m a wilderness and EMS emergency physician with particular sub specialties and a TV show. I need a website to highlight my interviews, teachings, etc... I did buy a number of domains for now.
Topics and things I need: CV (or version) me in the media, picture gallery, actually I sort of really like what dr owen parkes, my colleague has setup plus I have tv show and stuff like that. ridgeline tracker dot com

Target Market(s)

EMS, education, commercial products...

Industry/Entity Type

Medical And Science

Coding

Coded - Design and coding required

Number of Pages Required

1 page

Font styles to use
Sans Serif

Colors
f37122
9bcb3c
0556a4
a54499

Requirements
Must have
• Links and photos to news articles and things that mention me that I can add in.
Nice to have
• Maybe some snapshots of lecture reviews or patient thank you notes. Accolades so to speak
• I really appreciate how sharp it is. I would love to see Headings that resemble my friend's at ridgeline tracker dot com. Home, experience, consulting, lectures, affiliates, contact... those are main subjects... I think media also and that will have the TV show stuff and articles written about me...then maybe at the bottom of main page also have splits for training, research, television, and maybe exploration
Should not have
• The medical symbol with two snakes... that means quack doctor

```html
<!DOCTYPE html>
<html lang="en">
<head>
<meta charset="utf-8">
<title>Summit Field Care — Wilderness &amp; EMS Physician</title>
<link href="https://fonts.googleapis.com/css2?family=Raleway:ital,wght@0,400;0,500;0,600;0,700;1,400&family=Montserrat:wght@400;500;600&display=swap" rel="stylesheet">
<style>
  :root{
    --bg-dark:#333333;
    --bg-mid:#3a3a3a;
    --card:#3e3e3e;
    --heading-box:#303030;
    --text:#ffffff;
    --muted:#b9b9b9;
    --faint:#8a8a8a;
    --blue:#0556a4;
    --orange:#f37122;
    --green:#9bcb3c;
    --purple:#a54499;
    --track:#bdbdbd;
  }
  *{box-sizing:border-box;margin:0;padding:0}
  html,body{width:1200px;height:3746px;overflow:hidden}
  body{background:var(--bg-dark);color:var(--text);font-family:"Raleway",sans-serif;position:relative}
  .abs{position:absolute}
  section{position:absolute;left:0;width:1200px}

  /* header + hero */
  .hero{top:0;height:601px;background:var(--bg-dark)}
  .brand{left:160px;top:29px;display:flex;align-items:center;gap:12px}
  .brand-dot{width:68px;height:68px;border-radius:50%;background:#fff}
  .brand-name{font-family:"Montserrat",sans-serif;font-weight:600;font-size:15px;letter-spacing:1.5px;line-height:20px;color:#fff;text-transform:uppercase}
  .nav{left:477px;top:56px;display:flex;gap:0;font-size:12px;font-weight:500;text-transform:uppercase}
  .nav a{color:#fff;text-decoration:none;position:absolute;white-space:nowrap}
  .nav a.active{color:var(--blue);text-decoration:underline}
  .hero-photo{left:276px;top:128px;width:328px;height:473px;background:linear-gradient(180deg,#d9d2c8 0%,#e9edf2 40%,#c5d3e4 100%);border-radius:120px 120px 0 0}
  .hero-title{left:481px;top:268px;font-size:40px;font-weight:700;font-family:"Montserrat",sans-serif;letter-spacing:-0.5px;white-space:nowrap}
  .hero-title span{color:var(--blue)}
  .hero-sub{left:583px;top:325px;font-size:11px;font-style:italic;color:var(--muted)}
  .btn{display:flex;align-items:center;justify-content:center;font-family:"Montserrat",sans-serif;font-weight:600;font-size:9px;text-transform:uppercase;letter-spacing:.3px;color:#fff;background:var(--blue)}
  .btn-outline{background:transparent;border:1px solid var(--blue);color:var(--blue)}

  /* section heading */
  .sec-title{height:44px;background:var(--heading-box);display:flex;align-items:center;padding:0 21px;font-size:20px;font-weight:600;letter-spacing:1px;white-space:nowrap}

  /* about */
  .about{top:601px;height:662px;background:var(--bg-mid)}
  .about-back{left:160px;top:86px;width:358px;height:375px;background:repeating-linear-gradient(45deg,#2f2f2f 0 2px,#353535 2px 4px)}
  .about-frame{left:236px;top:61px;width:352px;height:349px;border:7px solid var(--blue);background:#fff;display:flex;justify-content:center;align-items:center}
  .about-photo{width:130px;height:300px;background:linear-gradient(180deg,#e3c8a8 0%,#f2f2f2 25%,#d8cdb6 70%,#3a3a3a 100%);border-radius:40px 40px 6px 6px}
  .about-text{left:634px;top:156px;width:405px;font-size:10px;line-height:22.5px;color:#e6e6e6}
  .about-text p+p{margin-top:11px}
  .skill{width:428px}
  .skill-label{font-size:9px;font-family:"Montserrat",sans-serif;color:#cfcfcf;text-transform:uppercase}
  .skill-pct{position:absolute;right:63px;top:-6px;font-size:9px;color:#cfcfcf}
  .skill-track{margin-top:9px;height:4px;background:var(--track);position:relative}
  .skill-fill{position:absolute;left:0;top:0;height:4px;width:89%;background:var(--blue)}

  /* services */
  .services{top:1263px;height:465px;background:var(--bg-dark)}
  .service{width:204px;height:199px;top:145px;text-align:center}
  .service.on{background:var(--card)}
  .service svg{display:block;margin:33px auto 0}
  .service h3{margin-top:17px;font-size:13px;font-weight:500;text-transform:uppercase}
  .service p{margin-top:9px;font-size:9.5px;line-height:22px;color:#dcdcdc;padding:0 24px}
  .dot{width:11px;height:11px;border-radius:50%;background:#777;top:392px}
  .dot.on{width:15px;height:15px;background:#fff;top:390px}

  /* work */
  .work{top:1728px;height:1119px;background:var(--bg-mid)}
  .filters{top:139px;left:0;width:1200px;font-size:12px;color:var(--faint)}
  .filters span{position:absolute}
  .filters .rule{width:22px;height:1px;background:var(--faint);top:8px}
  .tile{position:absolute}
  .tile-overlay{position:absolute;inset:0;background:rgba(30,30,30,.55)}
  .zoom{position:absolute;left:107px;top:257px;width:58px;height:58px;border-radius:50%;background:var(--orange);border:3px solid #f7a06b;display:flex;align-items:center;justify-content:center}

  /* resume */
  .resume{top:2847px;height:899px;background:var(--bg-dark)}
  .col-head{top:188px;display:flex;align-items:center;gap:14px;font-size:24px;font-weight:500;letter-spacing:1px}
  .cv-card{width:428px;height:169px;background:var(--card);padding:0 22px}
  .cv-date{margin-top:19px;font-size:8.5px;font-family:"Montserrat",sans-serif;color:var(--faint)}
  .cv-title{margin-top:14px;font-size:14.5px;font-weight:600;letter-spacing:.4px}
  .cv-text{margin-top:7px;font-size:9px;line-height:22px;color:var(--faint)}
  .cv-school{margin-top:5px;font-size:12.5px;font-weight:700}
  .cv-line{position:absolute;left:22px;right:22px;bottom:3px;height:2px}
</style>
</head>
<body>

<!-- header + hero -->
<section class="hero">
  <div class="abs brand">
    <div class="brand-dot"></div>
    <div class="brand-name">Summit<br>Field Care</div>
  </div>
  <nav class="abs nav">
    <a class="active" style="left:0">Home</a>
    <a style="left:66px">About</a>
    <a style="left:137px">Services</a>
    <a style="left:224px">Portfolio</a>
    <a style="left:320px">Resume-CV</a>
    <a style="left:420px">Blog-TV</a>
    <a style="left:503px">Contact</a>
  </nav>
  <div class="abs hero-photo" role="img" aria-label="Portrait of the physician in a white coat with stethoscope and clipboard"></div>
  <h1 class="abs hero-title"><span>Welcome</span> To My Website</h1>
  <p class="abs hero-sub">I am a wilderness and EMS emergency physician</p>
  <a class="abs btn" style="left:643px;top:368px;width:113px;height:44px">Learn More</a>
</section>

<!-- about -->
<section class="about">
  <div class="abs about-back"></div>
  <div class="abs about-frame">
    <div class="about-photo" role="img" aria-label="Full-length photo of the physician standing in a white coat"></div>
  </div>
  <h2 class="abs sec-title" style="left:634px;top:87px">About Me</h2>
  <div class="abs about-text">
    <p>Lorem ipsum dolor sit amet, consectetur adipisicing elit, sed do eiusmod adar tempor incidiei dunt ut labore et dolore magna aliqua. Ut enim ad minim loremit veniam, quis nostrud exeracita aation ullamco laboris nisi ut aliquip ex ea modo</p>
    <p>Lorem ipsum dolor sit amet, consectetur adipisicing elit, sed do eiusmod adar tempor incidiei dunt ut labore et dolore magna aliqua. Ut enim ad minim loremit veniam, quis nostrud exeracita aation ullamco laboris nisi ut aliquip ex ea modo</p>
  </div>
  <a class="abs btn" style="left:634px;top:340px;width:114px;height:44px">Hire Me</a>
  <a class="abs btn btn-outline" style="left:771px;top:340px;width:112px;height:44px">Download CV</a>

  <div class="abs skill" style="left:160px;top:528px"><div class="skill-label">Lorem ipsum dolor</div><span class="skill-pct">90%</span><div class="skill-track"><div class="skill-fill"></div></div></div>
  <div class="abs skill" style="left:611px;top:528px"><div class="skill-label">Lorem ipsum dolor</div><span class="skill-pct">90%</span><div class="skill-track"><div class="skill-fill"></div></div></div>
  <div class="abs skill" style="left:160px;top:578px"><div class="skill-label">Lorem ipsum dolor</div><span class="skill-pct">90%</span><div class="skill-track"><div class="skill-fill"></div></div></div>
  <div class="abs skill" style="left:611px;top:578px"><div class="skill-label">Lorem ipsum dolor</div><span class="skill-pct">90%</span><div class="skill-track"><div class="skill-fill"></div></div></div>
</section>

<!-- services -->
<section class="services">
  <h2 class="abs sec-title" style="left:529px;top:53px">My Services</h2>

  <div class="abs service on" style="left:161px">
    <svg width="28" height="30" viewBox="0 0 28 30" fill="none" stroke="#f37122" stroke-width="1.6"><circle cx="14" cy="8" r="5"/><path d="M9 5h10M4 29v-7c0-4 4-7 10-7s10 3 10 7v7z"/><path d="M14 15v8M11 20h6"/></svg>
    <h3>Lorem Ipsum</h3>
    <p>Godard kale chips tacos own thundercats normcore knau fat gaard kombucha tofu taxide</p>
  </div>
  <div class="abs service" style="left:385px">
    <svg width="30" height="30" viewBox="0 0 30 30" fill="none" stroke="#9bcb3c" stroke-width="1.6"><rect x="2" y="4" width="26" height="22"/><rect x="6" y="8" width="8" height="6"/><path d="M18 9h6M18 13h6M6 19h18M6 22h18"/></svg>
    <h3>Dolor Amet</h3>
    <p>Godard kale chips tacos own thundercats normcore knau fat gaard kombucha tofu taxide</p>
  </div>
  <div class="abs service" style="left:610px">
    <svg width="28" height="30" viewBox="0 0 28 30" fill="#0556a4"><rect x="4" y="6" width="20" height="24"/><rect x="10" y="1" width="8" height="6"/><rect x="12" y="10" width="4" height="8" fill="#333"/><rect x="10" y="12" width="8" height="4" fill="#333"/><rect x="11" y="23" width="6" height="7" fill="#333"/></svg>
    <h3>Valar Immy</h3>
    <p>Godard kale chips tacos own thundercats normcore knau fat gaard kombucha tofu taxide</p>
  </div>
  <div class="abs service" style="left:834px">
    <svg width="30" height="28" viewBox="0 0 30 28" fill="none" stroke="#a54499" stroke-width="1.6"><rect x="2" y="6" width="26" height="20"/><path d="M10 6V2h10v4M15 11v10M10 16h10"/></svg>
    <h3>Simply Dummy</h3>
    <p>Godard kale chips tacos own thundercats normcore knau fat gaard kombucha tofu taxide</p>
  </div>

  <span class="abs dot" style="left:570px"></span>
  <span class="abs dot on" style="left:592px"></span>
  <span class="abs dot" style="left:619px"></span>
</section>

<!-- latest work -->
<section class="work">
  <h2 class="abs sec-title" style="left:529px;top:52px">Latest Work</h2>
  <div class="abs filters">
    <span style="left:436px;color:var(--blue)">All</span>
    <span class="rule" style="left:476px"></span>
    <span style="left:520px">Lorem</span>
    <span class="rule" style="left:582px"></span>
    <span style="left:626px">Ipsum</span>
    <span class="rule" style="left:686px"></span>
    <span style="left:729px">Dolor</span>
  </div>

  <div class="tile" style="left:161px;top:182px;width:277px;height:278px;background:linear-gradient(160deg,#b9b8a8,#8a6a3c 55%,#d8b440)" role="img" aria-label="Firefighters treating a patient on a yellow tarp"></div>
  <div class="tile" style="left:461px;top:182px;width:278px;height:278px;background:linear-gradient(150deg,#9fb0c8,#c99a2c 50%,#3b3e4a)" role="img" aria-label="Rescue crew carrying a patient on an orange stretcher"></div>
  <div class="tile" style="left:761px;top:182px;width:278px;height:577px;background:linear-gradient(180deg,#8d9a92 0%,#c9c4bc 30%,#8f8a80 60%,#4f6e62 100%)" role="img" aria-label="Emergency crews working at a vehicle crash scene in a snowy field"></div>
  <div class="tile" style="left:161px;top:483px;width:277px;height:576px;background:linear-gradient(180deg,#6f746c 0%,#a9a59b 35%,#7a6b55 65%,#4f6e62 100%)" role="img" aria-label="Paramedics attending patients near an ambulance">
    <div class="tile-overlay"></div>
    <div class="zoom"><svg width="24" height="24" viewBox="0 0 24 24" fill="none" stroke="#fff" stroke-width="2.4"><circle cx="10" cy="10" r="6"/><path d="M14.5 14.5 21 21"/></svg></div>
  </div>
  <div class="tile" style="left:461px;top:483px;width:278px;height:276px;background:linear-gradient(180deg,#7b8b6e 0%,#a8b0ac 40%,#c9d233 70%,#8c8c8c 100%)" role="img" aria-label="Police and medics treating a casualty in front of a crowd"></div>
  <div class="tile" style="left:461px;top:784px;width:578px;height:275px;background:linear-gradient(120deg,#e8eef4 0%,#b9cee0 45%,#d7e2ec 75%,#6f7c88 100%)" role="img" aria-label="Doctors treating a patient on a hospital trolley"></div>
</section>

<!-- resume -->
<section class="resume">
  <h2 class="abs sec-title" style="left:529px;top:53px">Resume-CV</h2>

  <div class="abs col-head" style="left:163px">
    <svg width="40" height="30" viewBox="0 0 40 30" fill="#fff"><path d="M20 2 0 11l20 9 20-9z"/><path d="M8 16v8c3 4 21 4 24 0v-8l-12 6z"/><rect x="35" y="11" width="2" height="10"/></svg>
    <span>Education</span>
  </div>
  <div class="abs col-head" style="left:860px">
    <svg width="30" height="26" viewBox="0 0 30 26" fill="#fff"><path d="M10 5V1h10v4h-2V3h-6v2z"/><rect x="0" y="6" width="30" height="8"/><rect x="0" y="15" width="30" height="11"/></svg>
    <span>Experience</span>
  </div>

  <article class="abs cv-card" style="left:161px;top:235px">
    <p class="cv-date">February 2010-Present</p><h3 class="cv-title">Diploma In Lorem Ipsum Dolor Amet</h3>
    <p class="cv-text">Lorem ipsum dolor sit amet, consectetur adipisicing elit, sed do iusmodm incidi-<br>dunt ut labore et dolore magna aliqua</p>
    <p class="cv-school">University Of Lorem Ipsum</p><span class="cv-line" style="background:var(--orange)"></span>
  </article>
  <article class="abs cv-card" style="left:611px;top:235px">
    <p class="cv-date">February 2010-Present</p><h3 class="cv-title">Diploma In Lorem Ipsum Dolor Amet</h3>
    <p class="cv-text">Lorem ipsum dolor sit amet, consectetur adipisicing elit, sed do iusmodm incidi-<br>dunt ut labore et dolore magna aliqua</p>
    <p class="cv-school">University Of Lorem Ipsum</p><span class="cv-line" style="background:var(--green)"></span>
  </article>
  <article class="abs cv-card" style="left:161px;top:428px">
    <p class="cv-date">February 2010-Present</p><h3 class="cv-title">Diploma In Lorem Ipsum Dolor Amet</h3>
    <p class="cv-text">Lorem ipsum dolor sit amet, consectetur adipisicing elit, sed do iusmodm incidi-<br>dunt ut labore et dolore magna aliqua</p>
    <p class="cv-school">University Of Lorem Ipsum</p><span class="cv-line" style="background:var(--blue)"></span>
  </article>
  <article class="abs cv-card" style="left:611px;top:428px">
    <p class="cv-date">February 2010-Present</p><h3 class="cv-title">Diploma In Lorem Ipsum Dolor Amet</h3>
    <p class="cv-text">Lorem ipsum dolor sit amet, consectetur adipisicing elit, sed do iusmodm incidi-<br>dunt ut labore et dolore magna aliqua</p>
    <p class="cv-school">University Of Lorem Ipsum</p><span class="cv-line" style="background:var(--purple)"></span>
  </article>
  <article class="abs cv-card" style="left:161px;top:621px">
    <p class="cv-date">February 2010-Present</p><h3 class="cv-title">Diploma In Lorem Ipsum Dolor Amet</h3>
    <p class="cv-text">Lorem ipsum dolor sit amet, consectetur adipisicing elit, sed do iusmodm incidi-<br>dunt ut labore et dolore magna aliqua</p>
    <p class="cv-school">University Of Lorem Ipsum</p><span class="cv-line" style="background:var(--orange)"></span>
  </article>
  <article class="abs cv-card" style="left:611px;top:621px">
    <p class="cv-date">February 2010-Present</p><h3 class="cv-title">Diploma In Lorem Ipsum Dolor Amet</h3>
    <p class="cv-text">Lorem ipsum dolor sit amet, consectetur adipisicing elit, sed do iusmodm incidi-<br>dunt ut labore et dolore magna aliqua</p>
    <p class="cv-school">University Of Lorem Ipsum</p><span class="cv-line" style="background:var(--green)"></span>
  </article>
</section>

</body>
</html>
```